Business card for a shipping supplies business

Needing a business card design. Please see the logo. The logo with the white font should be used if there is a dark background.

We are looking for the following info on the card. Please see the sample info. We will need the info to be changed with a few different employee names and info but all will use the same template.

Business Name: The Crate Heron
Employee Name : Marcus Delaney
Position: Account Manager
Address: 4827 W. Ridge 418 S.
Fort Worth, TX 73948
email: Marcus@thecrateheron.example
telephone: 855-619-2740 x 207
website: www.getparcelkits.example

Target Market(s)

Businesses who ship products for online sales

Industry/Entity Type

Cardboard

Contact Information for Business Card

Name, title, address, website, logo, telephone number

Font styles to use
Sans Serif

Colors
EE7325
F08F49
F5BC92
FAE3D3
FDF4ED

Requirements
Must have
• Logo on back of card. Clean look, just logo, website address

```html
<!DOCTYPE html>
<html lang="en">
<head>
<meta charset="utf-8">
<title>The Crate Heron – Business Card</title>
<link rel="stylesheet" href="https://fonts.googleapis.com/css2?family=Montserrat:wght@500;600;700&family=Quicksand:wght@500&display=swap">
<style>
  :root {
    --backdrop: #985e3f;
    --card-dark: #1a1a1c;
    --card-tan: #c28c6a;
    --accent-orange: #d85a1e;
    --ink: #1a1a1c;
    --white: #ffffff;
  }
  html, body {
    margin: 0;
    padding: 0;
    width: 1200px;
    height: 1200px;
    overflow: hidden;
    background: var(--backdrop);
  }
  .canvas {
    position: relative;
    width: 1200px;
    height: 1200px;
  }
  .card {
    position: absolute;
    left: 196px;
    width: 809px;
    height: 462px;
    display: block;
  }
  .card--back { top: 132px; }
  .card--front { top: 606px; }
  .brand-name {
    font-family: "Montserrat", sans-serif;
    font-weight: 700;
    fill: var(--white);
  }
  .company {
    font-family: "Montserrat", sans-serif;
    font-weight: 500;
    fill: var(--ink);
  }
  .person-name {
    font-family: "Montserrat", sans-serif;
    font-weight: 600;
    fill: var(--ink);
  }
  .person-title {
    font-family: "Montserrat", sans-serif;
    font-weight: 500;
    fill: var(--ink);
  }
  .contact {
    font-family: "Quicksand", sans-serif;
    font-weight: 500;
    fill: var(--ink);
  }
  .icon { fill: var(--ink); }
</style>
</head>
<body>
<main class="canvas">

  <!-- Back of card: brand only -->
  <svg class="card card--back" viewBox="0 0 1011 577" aria-label="Card back">
    <defs>
      <filter id="panel-shadow" x="-10%" y="-10%" width="130%" height="130%">
        <feDropShadow dx="6" dy="0" stdDeviation="10" flood-color="#000" flood-opacity="0.45"/>
      </filter>
    </defs>
    <rect class="card-base" width="1011" height="577" fill="var(--card-tan)"/>
    <path class="dark-panel" filter="url(#panel-shadow)" fill="var(--card-dark)"
          d="M0 0 H730 L825 175 Q870 265 825 355 L690 577 H0 Z"/>
    <path class="panel-rule" fill="none" stroke="var(--card-tan)" stroke-width="5"
          d="M655 0 L760 190 Q800 265 760 340 L610 577"/>
    <rect class="brand-mark" x="290" y="160" width="110" height="110" rx="6" fill="var(--accent-orange)"/>
    <text class="brand-name" x="345" y="368" font-size="50" text-anchor="middle">CRATE HERON</text>
  </svg>

  <!-- Front of card: contact details -->
  <svg class="card card--front" viewBox="0 0 1011 577" aria-label="Card front">
    <defs>
      <filter id="panel-shadow-front" x="-10%" y="-10%" width="130%" height="130%">
        <feDropShadow dx="6" dy="0" stdDeviation="10" flood-color="#000" flood-opacity="0.45"/>
      </filter>
    </defs>
    <rect class="card-base" width="1011" height="577" fill="var(--card-tan)"/>
    <path class="dark-panel" filter="url(#panel-shadow-front)" fill="var(--card-dark)"
          d="M0 0 H370 L460 175 Q495 262 460 350 L330 577 H0 Z"/>
    <path class="panel-rule" fill="none" stroke="var(--card-tan)" stroke-width="5"
          d="M295 0 L395 190 Q430 262 395 335 L250 577"/>
    <rect class="brand-mark" x="150" y="190" width="90" height="90" rx="5" fill="var(--accent-orange)"/>
    <text class="brand-name" x="198" y="374" font-size="38" text-anchor="middle">CRATE HERON</text>

    <text class="company" x="990" y="160" font-size="50" text-anchor="end">The Crate Heron</text>
    <rect class="company-rule" x="536" y="182" width="475" height="3" fill="var(--ink)"/>
    <text class="person-name" x="536" y="236" font-size="39">Marcus Delaney</text>
    <text class="person-title" x="536" y="264" font-size="18">Account Manager</text>

    <!-- email -->
    <path class="icon" d="M531 316 H557 V331 H531 Z M533 318 L544 326 L555 318 Z" fill-rule="evenodd"/>
    <text class="contact" x="583" y="330" font-size="24">Marcus@thecrateheron.example</text>
    <!-- phone -->
    <path class="icon" d="M536 364 Q533 366 535 372 Q540 382 550 386 Q556 388 557 384 L558 381 L552 377 L549 380 Q543 377 541 371 L544 368 L540 362 Z"/>
    <text class="contact" x="583" y="382" font-size="24">855-619-2740 x 207</text>
    <!-- globe -->
    <g class="icon-globe" fill="none" stroke="var(--ink)" stroke-width="2">
      <circle cx="544" cy="426" r="12"/>
      <ellipse cx="544" cy="426" rx="5" ry="12"/>
      <line x1="532" y1="426" x2="556" y2="426"/>
      <line x1="534" y1="420" x2="554" y2="420"/>
      <line x1="534" y1="432" x2="554" y2="432"/>
    </g>
    <text class="contact" x="583" y="434" font-size="24">www.getparcelkits.example</text>
    <!-- pin -->
    <path class="icon" fill-rule="evenodd" d="M544 491 Q534 479 534 472 A10 10 0 0 1 554 472 Q554 479 544 491 Z M544 468 A4 4 0 1 0 544.01 468 Z"/>
    <text class="contact" x="580" y="490" font-size="20">4827 W. Ridge 418 S. Fort Worth, TX 73948</text>
  </svg>

</main>
</body>
</html>
```